Two Dating site user profile page redesign

Hi, Adobe XD designers.

I am looking for XD expert and professional web designer who can finish redesign of two user profile pages of a dating website.

I attached screenshots of the website profile page.

Note:
- The pages contents will be same. You can change layout, but not much. So I need similar layout and same contents in your new design.
- Design should be perfect in XD format, and it should match with logo color and homepage color styles. (Check attached files)
- I need two pages XD files in 24 hours after I hire you in a few hours.
- Designer should be able to redesign several pages more with me in two weeks after finish this first step. I will pay you per each page design.

I attached two files that looks good even though those were mobile app designs.

This dating site idea is "It's time for Singles".
Only require design experts who can finish quickly.

Thanks.

```html
<!DOCTYPE html>
<html lang="en">
<head>
<meta charset="utf-8">
<title>Edit my profile — Hearthly</title>
<link href="https://fonts.googleapis.com/css2?family=Poppins:wght@400;500;600&display=swap" rel="stylesheet">
<style>
:root{
  --red:#e3263f;
  --ink:#1f1f1f;
  --text:#4a4a4a;
  --muted:#6b6b6b;
  --line:#c9c9c9;
  --panel:#f2f2f2;
  --card:#ffffff;
  --photo-a:#c9b8a8;
  --photo-b:#6e5647;
}
*{box-sizing:border-box;margin:0;padding:0}
html,body{width:1200px;height:936px;overflow:hidden}
body{font-family:"Poppins",sans-serif;color:var(--ink);background:var(--card)}
.page{position:relative;width:1200px;height:936px}
.abs{position:absolute}

/* sidebar */
.brand{left:25px;top:16px;display:flex;align-items:center;gap:8px}
.brand-dot{width:22px;height:22px;border-radius:50%;background:var(--red)}
.brand-name{font-size:18px;font-weight:600;color:var(--red)}
.side-rule{left:0;top:93px;width:170px;height:1px;background:#e4e4e4}
.nav{left:0;top:102px;width:181px;list-style:none}
.nav li{position:relative;height:37.6px;display:flex;align-items:center;gap:12px;padding-left:24px;font-size:13px;color:var(--muted)}
.nav li svg{width:16px;height:16px;fill:none;stroke:currentColor;stroke-width:1.5}
.nav li.active{color:var(--red);font-weight:500}
.nav li.active::before{content:"";position:absolute;left:0;top:9px;width:3px;height:20px;background:var(--red)}

/* top bar */
.members{left:183px;top:10px;display:flex;align-items:center;gap:10px;font-size:12px}
.members b{background:var(--red);color:#fff;font-weight:500;font-size:12px;width:22px;height:22px;display:grid;place-items:center;border-radius:3px}
.topnav{right:12px;top:11px;display:flex;gap:34px;font-size:12px;color:var(--ink)}
.topnav span{display:flex;align-items:center;gap:9px}
.topnav svg{width:17px;height:17px;fill:none;stroke:var(--ink);stroke-width:1.5}

.panel{left:181px;top:44px;width:1019px;height:892px;background:var(--panel)}
.title{left:212px;top:61px;font-size:22px;font-weight:500}
.save{left:1107px;top:61px;width:62px;height:27px;border-radius:14px;background:var(--red);color:#fff;font-size:9px;font-weight:500;display:grid;place-items:center}
.section{font-size:21px;font-weight:500}
.card{background:var(--card);border-radius:14px}

.photo{left:225px;top:115px;width:106px;height:124px;border-radius:8px;background:linear-gradient(160deg,var(--photo-a),var(--photo-b))}
.name{left:349px;top:112px;font-size:19px;font-weight:500}
.meta{left:349px;top:137px;font-size:9px;color:var(--text);line-height:14px}

.lbl{font-size:11px;font-weight:500;color:var(--ink);line-height:14px}
.count{left:1127px;top:122px;width:30px;height:12px;border-radius:6px;background:#eee;font-size:7px;display:grid;place-items:center}
.area{border:1px solid #aaa;border-radius:8px;background:#fff}
.about-text{left:619px;top:141px;width:537px;height:86px;padding:10px 16px 0 12px;font-size:8.6px;line-height:13.3px;color:var(--ink)}
.grip{position:absolute;right:4px;bottom:3px;width:7px;height:7px;stroke:#888;fill:none}

.group{position:absolute}
.opts{list-style:none;margin-top:7px}
.opts li{height:15.6px;display:flex;align-items:center;gap:8px;font-size:9px;color:var(--text)}
.box,.radio{width:10px;height:10px;border:1px solid #8c8c8c;flex:none;position:relative}
.box{border-radius:2px}
.box.on{background:var(--red);border-color:var(--red)}
.box.on::after{content:"";position:absolute;left:2.5px;top:0.5px;width:3px;height:5.5px;border:solid #fff;border-width:0 1.5px 1.5px 0;transform:rotate(45deg)}
.radio{border-radius:50%}
.radio.on{border-color:var(--red)}
.radio.on::after{content:"";position:absolute;inset:1.5px;border-radius:50%;background:var(--red)}

.select,.input{position:absolute;height:20px;border:1px solid #a9a9a9;border-radius:2px;background:#fff;font-size:8.6px;color:var(--text);padding-left:7px;display:flex;align-items:center}
.select svg{position:absolute;right:7px;top:6px;width:10px;height:7px;fill:none;stroke:#555;stroke-width:1.4}
</style>
</head>
<body>
<div class="page">

  <div class="abs brand"><span class="brand-dot"></span><span class="brand-name">Hearthly</span></div>
  <div class="abs side-rule"></div>
  <ul class="abs nav">
    <li><svg viewBox="0 0 16 16"><rect x="1.5" y="3" width="13" height="10" rx="1"/><path d="M1.5 4l6.5 5 6.5-5"/></svg>Messages</li>
    <li class="active"><svg viewBox="0 0 16 16"><rect x="1.5" y="2.5" width="11" height="12" rx="1"/><path d="M7 10l1-3 6-6 2 2-6 6z"/></svg>Edit profile</li>
    <li><svg viewBox="0 0 16 16"><rect x="1.5" y="2.5" width="13" height="11" rx="1"/><path d="M2 12l4-4 3 3 2-2 3 3"/></svg>Photos</li>
    <li><svg viewBox="0 0 16 16"><rect x="1.5" y="1.5" width="13" height="13" rx="1"/><path d="M8 4.5l1 2.3 2.4.2-1.8 1.6.6 2.4L8 9.7 5.8 11l.6-2.4L4.6 7l2.4-.2z"/></svg>Favourites</li>
    <li><svg viewBox="0 0 16 16"><circle cx="8" cy="8" r="6.5"/><circle cx="8" cy="6" r="2"/><path d="M4.5 12.5c1-2 6-2 7 0"/></svg>Blacklist</li>
    <li><svg viewBox="0 0 16 16"><path d="M1.5 2.5h13v9h-8l-3 3v-3h-2z"/><path d="M4.5 6h7M4.5 8.5h5"/></svg>Comments</li>
    <li><svg viewBox="0 0 16 16"><path d="M3 15V2M3 2.5h10l-2 3 2 3H3"/></svg>Classifieds</li>
    <li><svg viewBox="0 0 16 16"><path d="M8 15s5-5 5-8.5a5 5 0 00-10 0C3 10 8 15 8 15z"/><circle cx="8" cy="6.5" r="1.8"/></svg>Tours</li>
    <li><svg viewBox="0 0 16 16"><path d="M1 8s2.5-5 7-5 7 5 7 5-2.5 5-7 5-7-5-7-5z"/><circle cx="8" cy="8" r="2"/></svg>Who viewed me</li>
    <li><svg viewBox="0 0 16 16"><circle cx="8" cy="8" r="2.2"/><circle cx="8" cy="8" r="5.5" stroke-dasharray="2.5 1.8"/></svg>Setting</li>
    <li><svg viewBox="0 0 16 16"><rect x="3" y="7" width="10" height="8" rx="1"/><path d="M5 7V5a3 3 0 016 0v2"/></svg>Privacy</li>
    <li><svg viewBox="0 0 16 16"><path d="M5 3.5a6 6 0 106 0M8 1v6"/></svg>Logout</li>
  </ul>

  <div class="abs members"><b>30</b>Registered members</div>
  <div class="abs topnav">
    <span><svg viewBox="0 0 16 16"><path d="M1 8s2.5-4.5 7-4.5S15 8 15 8s-2.5 4.5-7 4.5S1 8 1 8z"/><circle cx="8" cy="8" r="2"/></svg>Views</span>
    <span><svg viewBox="0 0 16 16"><rect x="1.5" y="3" width="13" height="10" rx="1"/><path d="M1.5 4l6.5 5 6.5-5"/></svg>Messages</span>
    <span><svg viewBox="0 0 16 16"><circle cx="8" cy="5" r="3"/><path d="M2 15c0-3.5 3-5 6-5s6 1.5 6 5"/></svg>My account<svg viewBox="0 0 16 16" style="width:12px"><path d="M3 6l5 5 5-5"/></svg></span>
  </div>

  <div class="abs panel"></div>
  <h1 class="abs title">Edit my profile</h1>
  <div class="abs save">Save</div>

  <!-- profile summary -->
  <div class="abs card" style="left:212px;top:101px;width:375px;height:150px"></div>
  <div class="abs photo" role="img" aria-label="Profile photo of the member"></div>
  <div class="abs name">Elodie</div>
  <div class="abs meta">Paris, Ile-de-France, France<br>11 August 1980, Leo, Straight, Woman</div>

  <div class="abs card" style="left:607px;top:101px;width:561px;height:150px"></div>
  <div class="abs lbl" style="left:619px;top:113px">About you</div>
  <div class="abs count">100</div>
  <div class="abs area about-text">Hailing from a working class family, I am Arjun. I am simple, sweet, confident and cunning fellow. My father is a renowned doctor who knows how to love his profession with passion and dedication. While my mother is a hardworking teacher at city public school whose only passion is to transform the lives of her students with knowledge and a good vision.<svg class="grip" viewBox="0 0 7 7"><path d="M1 6l5-5M4 6l2-2"/></svg></div>

  <h2 class="abs section" style="left:212px;top:270px">I am looking for</h2>
  <h2 class="abs section" style="left:680px;top:270px">About me</h2>

  <!-- looking for -->
  <div class="abs card" style="left:212px;top:311px;width:448px;height:234px"></div>
  <div class="group" style="left:231px;top:327px"><div class="lbl">Wish to meet</div>
    <ul class="opts"><li><i class="box"></i>Woman</li><li><i class="box on"></i>Man</li></ul></div>
  <div class="group" style="left:231px;top:390px"><div class="lbl">Preferred age</div>
    <ul class="opts"><li><i class="box"></i>18-20</li><li><i class="box on"></i>21-25</li><li><i class="box on"></i>26-30</li><li><i class="box"></i>31-35</li><li><i class="box"></i>36-40</li><li><i class="box"></i>41-50</li><li><i class="box"></i>61-80</li></ul></div>
  <div class="group" style="left:393px;top:327px"><div class="lbl">Purpose of dating</div>
    <ul class="opts"><li><i class="box on"></i>Friendship</li><li><i class="box"></i>Penpal</li><li><i class="box"></i>Flirt</li><li><i class="box"></i>Family</li><li><i class="box"></i>Traveling</li><li><i class="box"></i>Sport</li></ul></div>
  <div class="abs lbl" style="left:393px;top:448px">Whom I want to find</div>
  <div class="abs area" style="left:393px;top:471px;width:255px;height:62px"><svg class="grip" viewBox="0 0 7 7"><path d="M1 6l5-5M4 6l2-2"/></svg></div>

  <h2 class="abs section" style="left:212px;top:563px">Preferences in sex</h2>
  <div class="abs card" style="left:212px;top:605px;width:448px;height:282px"></div>
  <div class="group" style="left:231px;top:621px"><div class="lbl">What excites me</div>
    <ul class="opts"><li><i class="box"></i>Clothes</li><li><i class="box on"></i>Smell</li><li><i class="box"></i>Message</li><li><i class="box"></i>Photo and video</li><li><i class="box"></i>Role-playing game</li><li><i class="box"></i>Domination or submission</li><li><i class="box"></i>Other</li></ul></div>
  <div class="group" style="left:231px;top:762px"><div class="lbl">How often I would like to make sex</div>
    <ul class="opts"><li><i class="radio"></i>No answer</li><li><i class="radio"></i>Serval time a day</li><li><i class="radio"></i>At least on time a day</li><li><i class="radio on"></i>At least one time a week</li><li><i class="radio"></i>At least one time a month</li><li><i class="radio"></i>Sex is hot important to me</li></ul></div>
  <div class="group" style="left:449px;top:621px"><div class="lbl">Kind of sex like</div>
    <ul class="opts"><li><i class="box on"></i>Classical sex</li><li><i class="box on"></i>Virtual sex</li><li><i class="box"></i>Oral sex</li><li><i class="box"></i>Anal sex</li><li><i class="box"></i>Group sex</li><li><i class="box"></i>Public sex</li><li><i class="box"></i>Exchange of partners</li></ul></div>
  <div class="group" style="left:449px;top:762px"><div class="lbl">Finance support</div>
    <ul class="opts"><li><i class="radio"></i>No answer</li><li><i class="radio"></i>I am looking for a sponsor</li><li><i class="radio"></i>I am ready to be a sponsor</li><li><i class="radio on"></i>No need for a sponsor</li></ul></div>

  <!-- about me -->
  <div class="abs card" style="left:680px;top:311px;width:488px;height:562px"></div>
  <div class="abs lbl" style="left:692px;top:321px">Ethnicity</div>
  <div class="select" style="left:692px;top:339px;width:187px">Select<svg viewBox="0 0 10 7"><path d="M1 1l4 4 4-4"/></svg></div>
  <div class="abs lbl" style="left:965px;top:321px">Build</div>
  <div class="select" style="left:965px;top:339px;width:187px">Select<svg viewBox="0 0 10 7"><path d="M1 1l4 4 4-4"/></svg></div>
  <div class="abs lbl" style="left:692px;top:373px">Height</div>
  <div class="select" style="left:692px;top:391px;width:187px">5.4 ft (163-165 cm)<svg viewBox="0 0 10 7"><path d="M1 1l4 4 4-4"/></svg></div>
  <div class="abs lbl" style="left:965px;top:373px">Hair color</div>
  <div class="select" style="left:965px;top:391px;width:187px">Blonde<svg viewBox="0 0 10 7"><path d="M1 1l4 4 4-4"/></svg></div>
  <div class="abs lbl" style="left:692px;top:425px">Weight</div>
  <div class="select" style="left:692px;top:443px;width:187px">up to 40kg<svg viewBox="0 0 10 7"><path d="M1 1l4 4 4-4"/></svg></div>
  <div class="abs lbl" style="left:965px;top:425px">Sports</div>
  <div class="input" style="left:965px;top:443px;width:187px"></div>
  <div class="abs lbl" style="left:692px;top:477px">Hobbies</div>
  <div class="input" style="left:692px;top:495px;width:187px"></div>

  <div class="group" style="left:692px;top:529px"><div class="lbl">Relationship</div>
    <ul class="opts"><li><i class="radio"></i>No answer</li><li><i class="radio on"></i>No, I am single</li><li><i class="radio"></i>Nothing serious</li><li><i class="radio"></i>Yes, I have</li><li><i class="radio"></i>I am married</li></ul></div>
  <div class="group" style="left:855px;top:529px"><div class="lbl">Smoker</div>
    <ul class="opts"><li><i class="radio"></i>No answer</li><li><i class="radio"></i>Yes</li><li><i class="radio on"></i>No</li></ul></div>
  <div class="group" style="left:1017px;top:529px"><div class="lbl">Drinker</div>
    <ul class="opts"><li><i class="radio"></i>No answer</li><li><i class="radio"></i>Do not drink</li><li><i class="radio on"></i>Drink on holidays</li><li><i class="radio"></i>Drink often</li></ul></div>

  <div class="group" style="left:692px;top:640px"><div class="lbl">Education</div>
    <ul class="opts"><li><i class="radio"></i>No answer</li><li><i class="radio"></i>School</li><li><i class="radio on"></i>Some college</li><li><i class="radio"></i>High level</li><li><i class="radio"></i>Academic degree</li></ul></div>
  <div class="group" style="left:855px;top:640px"><div class="lbl">Occupation</div>
    <ul class="opts"><li><i class="radio"></i>No answer</li><li><i class="radio on"></i>Employee</li><li><i class="radio"></i>Self-employee</li><li><i class="radio"></i>Currently not employed</li><li><i class="radio"></i>Wealthy</li></ul></div>
  <div class="group" style="left:1017px;top:640px"><div class="lbl">Children</div>
    <ul class="opts"><li><i class="radio"></i>No answer</li><li><i class="radio on"></i>No</li><li><i class="radio"></i>No, but I want</li><li><i class="radio"></i>Yes, we live together</li><li><i class="radio"></i>Yes, we live apart</li></ul></div>

  <div class="group" style="left:692px;top:749px"><div class="lbl">Languages spoken</div>
    <ul class="opts"><li><i class="box on"></i>English</li><li><i class="box on"></i>German</li><li><i class="box"></i>French</li><li><i class="box"></i>Spanish</li><li><i class="box"></i>Italian</li><li><i class="box"></i>Other</li></ul></div>
  <div class="group" style="left:855px;top:749px"><div class="lbl">Place of residence</div>
    <ul class="opts"><li><i class="radio"></i>No answer</li><li><i class="radio"></i>Live alone in my house</li><li><i class="radio"></i>Live in a rented apartment</li><li><i class="radio on"></i>Live with parents</li><li><i class="radio"></i>Live with my boyfriend/girlfriend</li><li><i class="radio"></i>No Permanent residence</li></ul></div>

</div>
</body>
</html>
```